Korean Homemade food restaurant just like what your mom cooks at home

I need a black and white simple and modern design according to my logo.
My restaurant name is Nal Som (meaning of home cooking).
I need to have 늘찬(Nal Som) in Korean need to be included. Once again 늘찬.
I am not sure if I need to include my name and number and adress.
Updates

늘찬 Nal Som 478 Harwell Rd. Clarksville, TN 37118 Mark Yoon Owner Cell:931-608-2913 Store:931-617-3084

Target Market(s)

business owners, university students

Industry/Entity Type

Restaurant

Contact Information for Business Card

This is traditional Korean food restaurant that targets university students during lunch and Korean business travelers at dinner.

Font styles to use
Sans Serif

Requirements
Must have
• Must have my logo.

```html
<!DOCTYPE html>
<html lang="en">
<head>
<meta charset="utf-8">
<title>Nal Som — Business Card Concepts</title>
<link href="https://fonts.googleapis.com/css2?family=Jost:wght@400&family=Nanum+Myeongjo:wght@400&display=swap" rel="stylesheet">
<style>
  :root {
    --ink: #141414;
    --paper: #ffffff;
    --sheet-edge: #8a8a8a;
  }
  html, body {
    margin: 0;
    padding: 0;
    width: 1076px;
    height: 1200px;
    overflow: hidden;
    background: var(--paper);
  }
  .sheet {
    display: block;
    width: 1076px;
    height: 1200px;
  }
  .sheet-frame { fill: var(--paper); stroke: var(--sheet-edge); stroke-width: 1.5; }
  .card-outline { fill: none; stroke: var(--ink); stroke-width: 1.5; }
  .ink { fill: var(--ink); }
  .paper { fill: var(--paper); }
  .brand-name {
    font-family: "Jost", "Futura", sans-serif;
    font-weight: 400;
    text-anchor: middle;
  }
  .brand-korean {
    font-family: "Nanum Myeongjo", "Batang", serif;
    font-weight: 400;
    text-anchor: middle;
  }
</style>
</head>
<body>
<svg class="sheet" viewBox="0 0 1076 1200" xmlns="http://www.w3.org/2000/svg">
  <rect class="sheet-frame" x="4" y="4" width="1068" height="1192"/>

  <!-- Card front: white centre with vertical stripes -->
  <g class="card card-front" transform="translate(163 134)">
    <rect class="paper" width="751" height="418"/>
    <g class="stripes-left ink">
      <rect x="0" y="0" width="77" height="418"/>
      <rect x="86" y="0" width="8" height="418"/>
      <rect x="104" y="0" width="13" height="418"/>
      <rect x="126" y="0" width="9" height="418"/>
      <rect x="143" y="0" width="7" height="418"/>
      <rect x="160" y="0" width="5" height="418"/>
    </g>
    <g class="stripes-right ink" transform="translate(751 0) scale(-1 1)">
      <rect x="0" y="0" width="77" height="418"/>
      <rect x="86" y="0" width="8" height="418"/>
      <rect x="104" y="0" width="13" height="418"/>
      <rect x="126" y="0" width="9" height="418"/>
      <rect x="143" y="0" width="7" height="418"/>
      <rect x="160" y="0" width="5" height="418"/>
    </g>
    <rect class="card-outline" width="751" height="418"/>
    <circle class="brand-mark ink" cx="376" cy="124" r="50"/>
    <text class="brand-name ink" x="376" y="268" font-size="66">Nal Som</text>
    <text class="brand-korean ink" x="376" y="364" font-size="54">늘찬</text>
  </g>

  <!-- Card back: black centre band with horizontal stripes -->
  <g class="card card-back" transform="translate(163 649)">
    <rect class="paper" width="751" height="417"/>
    <g class="stripes ink">
      <rect x="0" y="20" width="751" height="24"/>
      <rect x="0" y="80" width="751" height="254"/>
      <rect x="0" y="370" width="751" height="24"/>
    </g>
    <rect class="card-outline" width="751" height="417"/>
    <circle class="brand-mark paper" cx="376" cy="131" r="38"/>
    <text class="brand-name paper" x="376" y="240" font-size="54">Nal Som</text>
    <text class="brand-korean paper" x="376" y="321" font-size="50">늘찬</text>
  </g>
</svg>
</body>
</html>
```